Geschäftspapiere für Bauunternehmung
Zielgruppe
Bauunternehmung, Zielgruppe sind Bauherren, Hausbesitzer
Aufgabenstellung
Guten Tag,
für mein Unternehmen benötige ich Geschäftspapiere in Form von Geschäftsbriefvorlage, Rechnungsvorlage und eine Angebotsvorlage diese sollten in Form eines Word-/Excelldocuments erstellt werden.
Folgende Kriterien sollten die erstellten Vorlagen erfüllen:
- Automatische und beim Öffnen des Dokumentes eine aktuelle Datumanzeige.
- Logo, Pflichtangaben wie Adresse, Firmensitz, Kontaktdaten, sollten fest eingebettet sein sodass diese sich nicht verziehen oder verrutschen dennoch aber änderbar sind sollte sich die Adresse oder die Rufnummer ändern.
- Summenfunktion der Geldwerte sollte integriert sein, sodass am Schluss die Gesamtsumme automatisch angezeigt wird.
- Mittels Tabulatortaste sollte man mit dem Cursor von Feld zu Feld springen können um diese auszufüllen.
- Zeilenabstand und Schriftart- und Größe sollten immer die gleichen sein.
- Sollte die Rechnungsvorlage über Excell erstellt werden. So sollten in der Maske Linien, Felder und Rahmen soweit wie möglich ausgeblendet werden sodass nur noch die Linien, Rahmen und Felder sichtbar erscheinen die benötigt werden.
- Faltzeichen sollten vorhanden sein.
Sollten Fragen zu meinen Anforderungen bestehen, so können wir dies im Vorfeld gerne besprechen.

```html
<!DOCTYPE html>
<html lang="de">
<head>
<meta charset="utf-8">
<title>Rechnung – Bravant Baugesellschaft mbH</title>
<link href="https://fonts.googleapis.com/css2?family=Open+Sans:wght@400;600;700&display=swap" rel="stylesheet">
<style>
  :root {
    --ink: #1d1d1b;
    --navy: #2c3550;
    --band-navy: #0f2f5c;
    --accent: #e2402a;
    --rule: #3a3a3a;
    --fold: #c8c8c8;
    --paper: #ffffff;
    --backdrop: #ffffff;
  }
  * { margin: 0; padding: 0; box-sizing: border-box; }
  html, body { width: 849px; height: 1200px; overflow: hidden; background: var(--backdrop); }
  body { font-family: "Open Sans", Arial, sans-serif; color: var(--ink); position: relative; }
  .sheet { position: absolute; left: 40px; top: 57px; width: 722px; height: 1021px; background: var(--paper); }
  .abs { position: absolute; }

  .brand { left: 360px; top: 52px; display: flex; align-items: center; gap: 14px; white-space: nowrap; }
  .brand-mark { flex: 0 0 auto; width: 50px; height: 50px; border-radius: 50%; background: var(--navy); }
  .brand-name { font-size: 17px; font-weight: 700; color: var(--navy); line-height: 1.1; }

  .sender-line { left: 64px; top: 149px; font-size: 6.6px; white-space: nowrap; }
  .recipient { left: 64px; top: 167px; font-size: 13.5px; line-height: 18px; font-style: normal; }
  .company { left: 455px; top: 138px; font-size: 13.5px; line-height: 17.7px; font-style: normal; }
  .company .mail { color: var(--accent); }

  .fold { left: 5px; width: 24px; height: 1px; background: var(--fold); }

  .doc-title { left: 72px; top: 384px; font-size: 17.5px; font-weight: 700; color: var(--accent); }
  .meta { left: 74px; top: 427px; width: 580px; font-size: 12px; }
  .meta span { position: absolute; white-space: nowrap; }

  .items { left: 68px; top: 461px; width: 591px; border-collapse: collapse; font-size: 12px; }
  .items th, .items td { font-weight: 400; height: 29.3px; padding: 0; white-space: nowrap; }
  .items thead th { border-top: 1px solid var(--rule); border-bottom: 1px solid var(--rule); }
  .items .num { width: 52px; text-align: center; }
  .items .desc { width: 223px; text-align: left; padding-left: 17px; }
  .items .unit { width: 113px; text-align: right; }
  .items .qty { width: 96px; text-align: right; }
  .items .total { text-align: right; padding-right: 4px; }
  .items .sum-label { text-align: left; padding-left: 5px; }
  .items tr.net td.sum-label, .items tr.net td.total { border-top: 1px solid var(--rule); }
  .items tr.grand td.sum-label, .items tr.grand td.total { border-top: 1px solid var(--rule); border-bottom: 1px solid var(--rule); height: 30px; }

  .footer-col { top: 912px; padding-left: 6px; border-left: 1px solid var(--accent); height: 80px; font-size: 9.7px; line-height: 13.4px; white-space: nowrap; }
  .footer-col strong { font-weight: 700; }
  .band { left: 0; top: 1005px; width: 722px; height: 16px; background: var(--band-navy); }
</style>
</head>
<body>
  <main class="sheet">
    <div class="abs brand">
      <span class="brand-mark"></span>
      <span class="brand-name">Bravant Baugesellschaft mbH</span>
    </div>

    <p class="abs sender-line">Bravant Baugesellschaft mbH | Musterstraße 26 | D – 892500 Musterstadt</p>
    <address class="abs recipient">
      Unser Kunde GmbH<br>Herr Mustermann<br>Musterstraße. 11<br>D-10111 Berlin
    </address>
    <address class="abs company">
      Bravant Baugesellschaft mbH<br>Musterstraße 26<br>72764 Musterstadt<br>
      Tel.&nbsp; 00000 / 30 00 000<br>Fax&nbsp; 00000 / 30 00 000<br>
      <span class="mail">info@bravant.de</span><br>www.bravant.de
    </address>

    <span class="abs fold" style="top:367px"></span>
    <span class="abs fold" style="top:713px"></span>

    <h1 class="abs doc-title">Rechnung</h1>
    <div class="abs meta">
      <span style="left:0">Rechnungsnummer: 2023-01111</span>
      <span style="left:241px">Kundennummer: 120023</span>
      <span style="right:0">24.07.2023</span>
    </div>

    <table class="abs items">
      <thead>
        <tr><th class="num">#</th><th class="desc">Beschreibung</th><th class="unit">Einzelpreis</th><th class="qty">Anzahl</th><th class="total">Gesamtpreis</th></tr>
      </thead>
      <tbody>
        <tr><td class="num">1</td><td class="desc">Erster Posten</td><td class="unit">12,00 €</td><td class="qty">2</td><td class="total">24,00 €</td></tr>
        <tr><td class="num">2</td><td class="desc">Zweiter Posten</td><td class="unit">7,50 €</td><td class="qty">2</td><td class="total">15,00 €</td></tr>
        <tr><td class="num">3</td><td class="desc">Dritter Posten</td><td class="unit">6,00 €</td><td class="qty">4</td><td class="total">24,00 €</td></tr>
        <tr><td class="num">4</td><td class="desc">Vierter Posten</td><td class="unit">10,00 €</td><td class="qty">3</td><td class="total">30,00 €</td></tr>
        <tr class="net"><td></td><td></td><td class="sum-label" colspan="2">Summe der Nettobeträge</td><td class="total">93,00 €</td></tr>
        <tr><td></td><td></td><td class="sum-label" colspan="2">zzgl. 19% Umsatzsteuer</td><td class="total">14,88 €</td></tr>
        <tr class="grand"><td></td><td></td><td class="sum-label" colspan="2">Gesamtbetrag</td><td class="total">107,88 €</td></tr>
      </tbody>
    </table>

    <div class="abs footer-col" style="left:79px">
      <strong>Bravant Bauunternehmen mbH</strong><br>Musterstrasse 10a<br>33397 Musterstadt<br>Tel.: +(49) 00000000000<br>Mobil: +(49) 00000000000
    </div>
    <div class="abs footer-col" style="left:285px">
      <strong>Bankverbindung:</strong><br>Muster Bank AG<br>DE 91 000000000000000000<br>BIC: ASDFR58
    </div>
    <div class="abs footer-col" style="left:482px">
      <strong>Amtsgericht:</strong><br>Musterstadt<br>USt-IdNr. DE0000000000000<br>Steuernummer: 000/0000/00000<br>Geschäftsführer: Muster
    </div>

    <div class="abs band" aria-hidden="true"></div>
  </main>
</body>
</html>
```